Talvera Web site

Talvera is a trade name for Dresgan enterprises llc, would like Dresgan mentioned but not prominent.

Use current logo to base colors and look/feel of website. Modern trendy look.

Talvera Technical Services - "Irrevocably committed to your success"

Website design for a nation wide service based company

Networking, AV, access control, automation, EAS, project management, consulting, electrical, design, service staffing

Hostwick hosts our URL's

Questions-
Who owns the content once accepted.
How is the content delivered to build site
How do we adjust. or add to content once published

Target Market(s)

commercial and retail technical services. IE, we provide technical services for retail and commercial vertical markets

Industry/Entity Type

Trade

Coding

Coded - Design and coding required

Number of Pages Required

5+ page

Font styles to use
Sans Serif

Colors
3276b5

Requirements
Must have
• Pages-
• About/info, contact, services, customers log in portal, social media links
• links to outside web based software portals
• Call through (call me) links

```html
<!DOCTYPE html>
<html lang="en">
<head>
<meta charset="utf-8">
<title>Talvera Technical Services</title>
<link href="https://fonts.googleapis.com/css2?family=Open+Sans:wght@400;600;700&family=Lora:ital@0;1&display=swap" rel="stylesheet">
<style>
:root{
  --blue:#3276b5;
  --blue-dark:#1f5c99;
  --blue-light:#5b95cc;
  --ink:#333b44;
  --muted:#6d747c;
  --line:#d9dde2;
  --bg-soft:#f3f4f6;
  --white:#ffffff;
}
*{box-sizing:border-box;margin:0;padding:0}
html,body{width:742px;height:1200px;overflow:hidden;background:var(--white)}
body{font-family:"Open Sans",Arial,sans-serif;color:var(--ink);position:relative}
.topbar{position:absolute;top:0;left:0;width:742px;height:30px;background:var(--bg-soft);border-bottom:1px solid var(--line);font-size:10px;color:var(--muted)}
.topbar .contact{position:absolute;left:40px;top:9px}
.topbar .social{position:absolute;right:40px;top:6px;display:flex;align-items:center;gap:6px}
.social .dot{width:17px;height:17px;border-radius:50%;background:var(--blue)}
.header{position:absolute;top:30px;left:0;width:742px;height:98px}
.brand{position:absolute;left:38px;top:20px;display:flex;align-items:center;gap:8px}
.brand .mark{width:34px;height:34px;border-radius:50%;background:var(--blue)}
.brand .name{font-weight:700;font-size:22px;color:var(--blue-dark);letter-spacing:1px}
.brand .tag{position:absolute;left:42px;top:30px;font-size:8px;color:var(--blue);letter-spacing:1px;white-space:nowrap}
.callus{position:absolute;right:40px;top:24px;display:flex;align-items:center;gap:8px;font-size:10px;color:var(--muted)}
.callus strong{font-size:20px;color:var(--blue-dark);font-weight:600}
.nav{position:absolute;right:40px;top:64px;display:flex;align-items:center;gap:22px;font-size:10px;font-weight:600;color:var(--ink)}
.nav .login{background:var(--blue);color:var(--white);padding:6px 12px;font-size:11px}
.hero{position:absolute;top:128px;left:0;width:742px;height:370px;background:linear-gradient(180deg,#c9c7bd 0%,#a8a596 45%,#6e6a5d 75%,#3d3b35 100%)}
.hero .headline{position:absolute;left:256px;top:122px;font-family:"Lora",Georgia,serif;font-size:26px;line-height:32px;color:var(--white)}
.hero .dots{position:absolute;left:340px;top:346px;display:flex;gap:6px}
.hero .dots span{width:12px;height:12px;border-radius:50%;border:2px solid var(--white)}
.hero .dots span.on{background:var(--white)}
.section-title{position:absolute;left:0;width:742px;text-align:center;font-size:13px;font-weight:700;color:var(--blue)}
.section-title small{display:block;font-size:7px;color:var(--muted);font-weight:400;letter-spacing:2px}
.services{position:absolute;top:560px;left:60px;width:622px;display:flex;justify-content:space-between}
.service{width:190px;display:flex;gap:10px}
.service .icon{flex:none;width:38px;height:38px;border-radius:50%;border:2px solid var(--blue);display:flex;align-items:center;justify-content:center}
.service h3{font-size:11px;font-weight:700;margin-bottom:4px}
.service p{font-size:9px;line-height:13px;color:var(--muted)}
.service .more{display:block;margin-top:4px;font-size:9px;color:var(--blue);font-weight:600}
.arrow{position:absolute;top:585px}
.welcome{position:absolute;top:690px;left:0;width:742px;height:160px;background:linear-gradient(90deg,var(--blue-dark),var(--blue) 50%,var(--blue-light));color:var(--white);text-align:center}
.welcome h2{margin-top:24px;font-size:13px;font-weight:700}
.welcome p{width:560px;margin:12px auto 0;font-size:10px;line-height:16px}
.btn{display:inline-block;border:1px solid currentColor;padding:6px 16px;font-size:9px;font-weight:600;letter-spacing:1px}
.welcome .btn{margin-top:14px}
.testimonials{position:absolute;top:905px;left:60px;width:622px;display:flex;justify-content:space-between;text-align:center}
.person{width:180px}
.person .photo{width:72px;height:72px;border-radius:50%;margin:0 auto 8px;background:linear-gradient(135deg,#b08d70,#5b4537)}
.person h4{font-size:10px;font-weight:700}
.person .place{font-size:8px;color:var(--muted);margin-bottom:6px}
.person p{font-size:9px;line-height:13px;color:var(--muted)}
.testi-more{position:absolute;top:1068px;left:0;width:742px;text-align:center;color:var(--blue)}
.footer{position:absolute;top:1115px;left:0;width:742px;height:85px;border-top:1px solid var(--line)}
.footer .brand-sub{position:absolute;left:40px;top:20px;display:flex;align-items:center;gap:8px}
.brand-sub .mark{width:26px;height:26px;background:var(--blue)}
.brand-sub .name{font-weight:700;font-size:14px;color:var(--blue-dark)}
.brand-sub .sub{font-size:7px;color:var(--muted);letter-spacing:1px}
.footer .links{position:absolute;right:40px;top:28px;font-size:9px;color:var(--ink)}
.footer .copy{position:absolute;right:40px;top:44px;font-size:8px;color:var(--muted)}
</style>
</head>
<body>
<div class="topbar">
  <div class="contact">E-mail Us: info@talvera.com</div>
  <div class="social"><span>Follow us on</span><span class="dot"></span><span class="dot"></span><span class="dot"></span></div>
</div>

<header class="header">
  <div class="brand">
    <span class="mark"></span>
    <span class="name">TALVERA</span>
    <span class="tag">TECHNICAL SERVICES</span>
  </div>
  <div class="callus">
    <svg width="14" height="14" viewBox="0 0 24 24"><path fill="#6d747c" d="M6.6 10.8a15 15 0 0 0 6.6 6.6l2.2-2.2c.3-.3.7-.4 1-.2 1.1.4 2.3.6 3.6.6.6 0 1 .4 1 1V20c0 .6-.4 1-1 1A17 17 0 0 1 3 4c0-.6.4-1 1-1h3.5c.6 0 1 .4 1 1 0 1.3.2 2.5.6 3.6.1.3 0 .7-.2 1z"/></svg>
    <span>Call Us Now on</span><strong>414.555.0190</strong>
  </div>
  <nav class="nav">
    <span>HOME</span><span>ABOUT US</span><span>SERVICES</span><span>TESTIMONIALS</span><span>CONTACT</span>
    <span class="login">Customer Log In</span>
  </nav>
</header>

<section class="hero" role="img" aria-label="Businessman walking toward a sunlit horizon along a road marked with the word success">
  <div class="headline">Irrevocably committed<br>to your success</div>
  <div class="dots"><span class="on"></span><span></span><span></span><span></span></div>
</section>

<h2 class="section-title" style="top:518px">OUR SERVICES<small>———</small></h2>
<svg class="arrow" style="left:28px" width="12" height="20" viewBox="0 0 12 20"><path d="M10 2 2 10l8 8" fill="none" stroke="#333b44" stroke-width="2.5"/></svg>
<svg class="arrow" style="right:28px" width="12" height="20" viewBox="0 0 12 20"><path d="M2 2l8 8-8 8" fill="none" stroke="#333b44" stroke-width="2.5"/></svg>
<div class="services">
  <div class="service">
    <span class="icon"><svg width="20" height="20" viewBox="0 0 20 20" fill="none" stroke="#3276b5" stroke-width="1.6"><circle cx="10" cy="4" r="2.5"/><circle cx="4" cy="15" r="2.5"/><circle cx="16" cy="15" r="2.5"/><path d="M10 6.5v4M10 10.5 5.5 13M10 10.5l4.5 2.5"/></svg></span>
    <div><h3>NETWORKING</h3><p>Ordinary to popular belief, sample text is not simply random words. It has roots in a piece of classic writing from 45 BC.</p><span class="more">Read More ›</span></div>
  </div>
  <div class="service">
    <span class="icon"><svg width="20" height="20" viewBox="0 0 20 20" fill="none" stroke="#3276b5" stroke-width="1.8"><circle cx="8" cy="8" r="5"/><path d="M12 12l5 5"/></svg></span>
    <div><h3>ACCESS CONTROL</h3><p>Ordinary to popular belief, sample text is not simply random words. It has roots in a piece of classic writing from 45 BC.</p><span class="more">Read More ›</span></div>
  </div>
  <div class="service">
    <span class="icon"><svg width="20" height="20" viewBox="0 0 20 20" fill="none" stroke="#3276b5" stroke-width="1.6"><circle cx="10" cy="10" r="3"/><path d="M10 2v3M10 15v3M2 10h3M15 10h3M4.3 4.3l2.1 2.1M13.6 13.6l2.1 2.1M4.3 15.7l2.1-2.1M13.6 6.4l2.1-2.1"/></svg></span>
    <div><h3>AUTOMATION</h3><p>Ordinary to popular belief, sample text is not simply random words. It has roots in a piece of classic writing from 45 BC.</p><span class="more">Read More ›</span></div>
  </div>
</div>

<section class="welcome">
  <h2>WELCOME TO OUR SITE</h2>
  <p>Contrary to popular belief, sample text is not simply random text. It has roots in a piece of classical writing from 45 BC, making it over 2000 years old. Edwin Harrow, a Latin professor at Ashford College in Virginia, looked up one of the more obscure Latin words, consectetur.</p>
  <span class="btn">READ MORE</span>
</section>

<h2 class="section-title" style="top:866px">TESTIMONIALS<small>———</small></h2>
<div class="testimonials">
  <div class="person">
    <div class="photo" role="img" aria-label="Portrait photo of a client"></div>
    <h4>MARCO DELVIN</h4><div class="place">Australia</div>
    <p>There are many variations of passages of sample text available, but the majority have suffered alteration in some form.</p>
  </div>
  <div class="person">
    <div class="photo" role="img" aria-label="Portrait photo of a client"></div>
    <h4>AARON KEEL</h4><div class="place">Australia</div>
    <p>Contrary to popular belief, sample text is not simply random text. It has roots in a piece of classical literature.</p>
  </div>
  <div class="person">
    <div class="photo" role="img" aria-label="Portrait photo of a client"></div>
    <h4>LANE</h4><div class="place">Australia</div>
    <p>The standard chunk of sample text used since the 1500s is reproduced below for those interested. Sections.</p>
  </div>
</div>
<div class="testi-more"><span class="btn">READ MORE</span></div>

<footer class="footer">
  <div class="brand-sub">
    <span class="mark"></span>
    <div><div class="name">DRESGAN</div><div class="sub">ENTERPRISES LLC</div></div>
  </div>
  <div class="links">Home / About us / Services / Customer Log in / Testimonials / Contact</div>
  <div class="copy">Copyright © 2015 All Rights Reserved</div>
</footer>
</body>
</html>
```